Brightmoor Card Company Business Cards

We are a trading card store with Zorblix, sports and other TCG cards, we need a business card design that encompasses a clean cut, modern style with a retro flare. website is brightmoorcardco.com for reference. Can utilize a comic book era feel or a more modern outdoor feel to utilize the "Pacific Northwest" elements of tress, mountains, etc.

Industry/Entity Type

Trading cards and collectibles

Contact Information for Business Card

business name, email address, phone number, name, owner job title

Font styles to use
Sans Serif

```html
<!DOCTYPE html>
<html lang="en">
<head>
<meta charset="utf-8">
<title>Brightmoor Card Company – Business Cards</title>
<link rel="stylesheet" href="https://fonts.googleapis.com/css2?family=Roboto:wght@400;700&display=swap">
<style>
  :root {
    --page: #e9e9e7;
    --card-white: #ffffff;
    --slate: #6b6b6b;
    --slate-deep: #5f5f5f;
    --slate-light: #9a9a9a;
    --cyan: #1bb3d6;
    --ink: #555555;
  }
  * { box-sizing: border-box; margin: 0; padding: 0; }
  html, body {
    width: 1200px; height: 716px; overflow: hidden;
    background: var(--page);
    font-family: "Roboto", Arial, sans-serif;
  }
  .sheet {
    position: relative; width: 1200px; height: 716px;
    display: flex; align-items: center; justify-content: center; gap: 40px;
  }
  .card {
    position: relative; width: 540px; height: 310px;
    border-radius: 22px; overflow: hidden;
    box-shadow: 0 6px 18px rgba(0,0,0,0.18);
  }

  /* Front */
  .card--front { background: var(--card-white); }
  .holder { position: absolute; left: 44px; top: 38px; }
  .holder__name {
    color: var(--cyan); font-weight: 700; font-size: 22px;
    text-transform: uppercase; letter-spacing: 0.4px; line-height: 1.1;
  }
  .holder__title { color: var(--slate-light); font-size: 12px; margin-top: 2px; }
  .contact { position: absolute; left: 44px; top: 100px; list-style: none; }
  .contact__item {
    display: flex; align-items: center; gap: 8px;
    font-size: 13px; color: var(--ink); line-height: 19px;
  }
  .contact__icon { width: 11px; height: 11px; flex: none; fill: var(--cyan); }
  .range {
    position: absolute; inset: 0;
    background: linear-gradient(180deg, #767676 0%, var(--slate) 60%, var(--slate-deep) 100%);
    clip-path: polygon(0 76%, 100% 34%, 100% 100%, 0 100%);
  }

  /* Back */
  .card--back { background: var(--slate); }
  .peak {
    position: absolute; inset: 0;
    background: linear-gradient(110deg, #ffffff 0%, #f6f6f6 55%, #e4e4e4 100%);
    clip-path: polygon(0 22%, 34% 12%, 72% 100%, 0 100%);
  }
  .brand {
    position: absolute; left: 336px; right: 20px; top: 50%;
    transform: translateY(-50%);
    display: flex; align-items: center; gap: 10px;
  }
  .brand__dot {
    width: 14px; height: 14px; border-radius: 50%;
    background: var(--cyan); flex: none;
  }
  .brand__name {
    color: var(--card-white); font-weight: 700; font-size: 22px;
    line-height: 1.15; text-transform: uppercase; letter-spacing: 1px;
  }
</style>
</head>
<body>
<main class="sheet">
  <section class="card card--front" aria-label="Business card front">
    <div class="range" role="img" aria-label="Grey Pacific Northwest mountain range rising toward the right edge"></div>
    <div class="holder">
      <p class="holder__name">Ellis Marlow</p>
      <p class="holder__title">President</p>
    </div>
    <ul class="contact">
      <li class="contact__item">
        <svg class="contact__icon" viewBox="0 0 12 12" aria-hidden="true"><path d="M2.5 0.5 L4.5 0.5 L5.2 3 L3.8 4.2 C4.5 5.8 6 7.4 7.8 8.2 L9 6.8 L11.5 7.5 L11.5 9.5 C11.5 10.8 10.5 11.5 9.5 11.5 C4.5 11 1 7.5 0.5 2.5 C0.5 1.4 1.3 0.5 2.5 0.5 Z"/></svg>
        <span>736-555-0192</span>
      </li>
      <li class="contact__item">
        <svg class="contact__icon" viewBox="0 0 12 12" aria-hidden="true"><path d="M0 2 H12 V10 H0 Z M0.8 2.6 L6 6.6 L11.2 2.6" stroke="#fff" stroke-width="0.8"/></svg>
        <span>info@brightmoorcardco.com</span>
      </li>
      <li class="contact__item">
        <svg class="contact__icon" viewBox="0 0 12 12" aria-hidden="true"><circle cx="6" cy="6" r="6"/><path d="M0 6 H12 M6 0 C3 3 3 9 6 12 M6 0 C9 3 9 9 6 12" stroke="#fff" stroke-width="0.8" fill="none"/></svg>
        <span>www.brightmoorcardco.com</span>
      </li>
    </ul>
  </section>

  <section class="card card--back" aria-label="Business card back">
    <div class="peak" role="img" aria-label="Large white snow-covered mountain peak rising from the lower left on grey"></div>
    <div class="brand">
      <span class="brand__dot" aria-hidden="true"></span>
      <p class="brand__name">Brightmoor<br>Card Company</p>
    </div>
  </section>
</main>
</body>
</html>
```